'The Brookfield' @2847 Marlow Bend Road, Greenwith

Hi, We need a For Sale brochure done for a new land division. I work in Real Estate and have have listed 14 Land Allotments and would like a nice brochure done.

The land is near some green hills and the site use to be called the Kitty Haven. I thought the development could be called 'The Brookfield' 14 Premium Allotments Greenwith.

The design we would like the name of the development across the front. Some hills, or sunset, something to represent lifestyle living.

Write Up:
Premium 14 Allotments For Sale
Blocks 359m2 - 496m2

The Brookfield offers; Sunning view to the hills, convenient location to local shops, transport and schools.

Build your dream home in this premium location on the ideal sized allotment.

Be apart of something special The Brookfield Allotments will sell quickly only 14 Available

Target Market(s)

Property Buyers looking to build their dream home on a nice block of land

Industry/Entity Type

Real Estate

Colors
add136

Requirements
Must have
• Logo, Address, Some Hills, Our company details and logo,
Nice to have
• Green Hills or sunset. Professional brochure.

```html
<!DOCTYPE html>
<html lang="en">
<head>
<meta charset="UTF-8">
<title>The Brookfield – Allotments Brochure</title>
<link rel="stylesheet" href="https://fonts.googleapis.com/css2?family=Parisienne&family=Questrial&family=Arimo:wght@400;700&display=swap">
<style>
  :root {
    --page-bg: #ffffff;
    --brand-green: #00a651;
    --wave-lime: #a6ce39;
    --wave-yellow: #fff212;
    --sky-top: #4a9de6;
    --sky-low: #a9d2f4;
    --hill-tan: #a89b78;
    --bush-green: #6b8744;
    --grass-dry: #aea686;
    --ink-dark: #333333;
    --title-white: #ffffff;
    --frame-line: #555555;
  }
  * { margin: 0; padding: 0; box-sizing: border-box; }
  html, body {
    width: 1200px;
    height: 1000px;
    overflow: hidden;
    background: var(--page-bg);
  }
  .brochure {
    position: absolute;
    left: 278px;
    top: 45px;
    width: 643px;
    height: 909px;
    border: 1px solid var(--frame-line);
    overflow: hidden;
  }
  .brochure-art {
    position: absolute;
    inset: 0;
    width: 643px;
    height: 909px;
    display: block;
  }
  .tagline {
    position: absolute;
    left: 34px;
    top: 40px;
    width: 560px;
    font-family: "Parisienne", cursive;
    font-size: 31px;
    line-height: 56px;
    color: var(--ink-dark);
  }
  .development-name {
    position: absolute;
    right: 38px;
    top: 592px;
    font-family: "Questrial", sans-serif;
    font-size: 70px;
    line-height: 80px;
    color: var(--title-white);
    white-space: nowrap;
  }
  .features {
    position: absolute;
    right: 35px;
    top: 676px;
    width: 340px;
    text-align: right;
    font-family: "Arimo", sans-serif;
    font-size: 15px;
    line-height: 20px;
    color: var(--ink-dark);
  }
  .agency-badge {
    position: absolute;
    left: 165px;
    top: 791px;
    width: 314px;
    height: 91px;
    background: var(--wave-lime);
    display: flex;
    align-items: center;
    justify-content: center;
  }
  .agency-name {
    font-family: "Arimo", sans-serif;
    font-weight: 700;
    font-size: 22px;
    letter-spacing: 1px;
    color: var(--title-white);
    text-transform: uppercase;
  }
</style>
</head>
<body>
  <main class="brochure">
    <svg class="brochure-art" viewBox="0 0 643 909" xmlns="http://www.w3.org/2000/svg">
      <defs>
        <linearGradient id="landscape-tones" x1="0" y1="0" x2="0" y2="1">
          <stop offset="0" stop-color="var(--sky-top)"/>
          <stop offset="0.33" stop-color="var(--sky-low)"/>
          <stop offset="0.36" stop-color="var(--hill-tan)"/>
          <stop offset="0.55" stop-color="var(--bush-green)"/>
          <stop offset="0.8" stop-color="var(--bush-green)"/>
          <stop offset="1" stop-color="var(--grass-dry)"/>
        </linearGradient>
      </defs>
      <rect class="hero-photo" x="0" y="0" width="643" height="500" fill="url(#landscape-tones)"
            role="img" aria-label="Photo of green rolling hills with native trees and dry grass under a clear blue sky"/>
      <path class="wave-lime" fill="var(--wave-lime)"
            d="M0,462 C180,470 420,320 560,365 C600,372 630,380 643,392 L643,909 L0,909 Z"/>
      <path class="wave-yellow" fill="var(--wave-yellow)"
            d="M0,540 C250,545 420,400 560,395 C600,395 630,405 643,412 L643,909 L0,909 Z"/>
      <path class="panel-green" fill="var(--brand-green)"
            d="M0,648 C250,630 420,430 560,425 C600,424 630,432 643,440 L643,909 L0,909 Z"/>
    </svg>

    <p class="tagline">Build your dream home in this premium location on the ideal sized allotment.</p>

    <h1 class="development-name">The Brookfield</h1>

    <p class="features">Sunning view to the hills,<br>convenient location to local shops,<br>transport and schools.</p>

    <div class="agency-badge">
      <span class="agency-name">Harlow Reid Real Estate</span>
    </div>
  </main>
</body>
</html>
```